Nectarine Point of Sale Cards for Grocery Retail Markets

We are looking to update our Nectarine point of sale card and price card. The cards will need to be 7" x 11" with a .125 bleed - one sided. See attached for the old versions. We would like this to use photos that look like true Washington State Peaches. Here are the bullet points we would like to use: - New Crop!- Tree Ripened- Excellent FlavorNOTE: The price card just needs to have a space where a retailer can write in the sale price of the item. See attachment with the white box.

Target Market(s)

Retail market shoppers

Requirements
Must have
• Pictures of Nectarines Only

```html
<!DOCTYPE html>
<html lang="en">
<head>
<meta charset="utf-8">
<title>Nectarine Point of Sale Card</title>
<link rel="stylesheet" href="https://fonts.googleapis.com/css2?family=Bebas+Neue&family=Yesteryear&family=Ubuntu:wght@500;700&display=swap">
<style>
  :root {
    --canvas-bg: #474747;
    --card-green: #2f7d56;
    --banner-orange: #e04a26;
    --stripe-red: #8a1e1a;
    --text-white: #ffffff;
    --brand-green: #1f6b43;
    --peach-deep: #d2462a;
    --peach-mid: #ee8a3c;
    --peach-light: #f6c463;
  }
  * { margin: 0; padding: 0; box-sizing: border-box; }
  html, body { width: 1200px; height: 1200px; overflow: hidden; }
  body { background: var(--canvas-bg); position: relative; }

  .pos-card {
    position: absolute;
    left: 80px; top: 269px;
    width: 1040px; height: 662px;
    overflow: hidden;
    background: var(--card-green);
  }
  .card-art { position: absolute; inset: 0; width: 100%; height: 100%; }

  .headline {
    position: absolute; left: 26px; top: 38px;
    color: var(--text-white);
    font-family: "Bebas Neue", "Oswald", sans-serif;
    line-height: 0.86;
  }
  .headline__region { display: block; font-size: 92px; letter-spacing: 0.5px; }
  .headline__product { display: block; font-size: 146px; letter-spacing: 1px; margin-top: 4px; }

  .tagline-band {
    position: absolute; left: 0; top: 256px;
    width: 627px; height: 78px;
    background: var(--banner-orange);
  }
  .tagline-band__text {
    position: absolute; left: 22px; top: 2px;
    color: var(--text-white);
    font-family: "Yesteryear", cursive;
    font-size: 64px; line-height: 78px;
    white-space: nowrap;
  }

  .feature-list {
    position: absolute; left: 30px; top: 342px;
    list-style: none;
    color: var(--text-white);
    font-family: "Ubuntu", sans-serif;
    font-weight: 500; font-size: 35px;
  }
  .feature-list__item { display: flex; align-items: center; height: 53px; }
  .feature-list__tick { width: 22px; height: 22px; margin-right: 20px; flex: none; }

  .price-line {
    position: absolute; left: 52px; top: 592px;
    width: 208px; border-top: 2px dotted rgba(255,255,255,0.8);
  }

  .brand-box {
    position: absolute; left: 718px; top: 31px;
    width: 303px; height: 96px;
    background: #ffffff;
    display: flex; align-items: center;
    padding: 0 16px;
  }
  .brand-box__dot {
    width: 62px; height: 62px; border-radius: 50%;
    background: var(--peach-deep); flex: none; margin-right: 14px;
  }
  .brand-box__name {
    color: var(--brand-green);
    font-family: "Ubuntu", sans-serif;
    font-weight: 700; font-size: 19px; line-height: 1.1;
  }
</style>
</head>
<body>
  <section class="pos-card">
    <svg class="card-art" viewBox="0 0 1040 662" preserveAspectRatio="none">
      <defs>
        <radialGradient id="peachTone" cx="0.55" cy="0.62" r="0.6">
          <stop offset="0" stop-color="var(--peach-deep)"/>
          <stop offset="0.55" stop-color="var(--peach-mid)"/>
          <stop offset="1" stop-color="var(--peach-light)"/>
        </radialGradient>
      </defs>
      <rect x="0" y="0" width="1040" height="662" fill="url(#peachTone)" role="img" aria-label="Photograph of a ripe nectarine close up"/>
      <polygon points="0,0 730,0 275,662 0,662" fill="var(--card-green)"/>
      <polygon points="500,334 560,334 345,662 275,662" fill="var(--stripe-red)"/>
    </svg>

    <h1 class="headline">
      <span class="headline__region">Washimgton State</span>
      <span class="headline__product">Nectarines</span>
    </h1>

    <div class="tagline-band">
      <p class="tagline-band__text">Taste the Difference!</p>
    </div>

    <ul class="feature-list">
      <li class="feature-list__item">
        <svg class="feature-list__tick" viewBox="0 0 22 22"><rect x="1" y="5" width="15" height="15" fill="none" stroke="#fff" stroke-width="2"/><path d="M4 12l4 4 12-13" fill="none" stroke="#fff" stroke-width="3"/></svg>
        New Crop !
      </li>
      <li class="feature-list__item">
        <svg class="feature-list__tick" viewBox="0 0 22 22"><rect x="1" y="5" width="15" height="15" fill="none" stroke="#fff" stroke-width="2"/><path d="M4 12l4 4 12-13" fill="none" stroke="#fff" stroke-width="3"/></svg>
        Tree Ripened
      </li>
      <li class="feature-list__item">
        <svg class="feature-list__tick" viewBox="0 0 22 22"><rect x="1" y="5" width="15" height="15" fill="none" stroke="#fff" stroke-width="2"/><path d="M4 12l4 4 12-13" fill="none" stroke="#fff" stroke-width="3"/></svg>
        Excellent Flavor
      </li>
    </ul>

    <div class="price-line"></div>

    <div class="brand-box">
      <span class="brand-box__dot"></span>
      <span class="brand-box__name">Evergreen Orchard<br>Growers Board</span>
    </div>
  </section>
</body>
</html>
```